Stationary for New Company

We need stationary designed for a new company. Details of the required stationary is attached.

The final version should be trendy, clean... only 2 colours (green + grey/black) and professional.

#1: Business Cards (design on 2 sides)
#2: Letterhead (word format)
#3: Cover Page and back cover for proposals
#4: Envelopes,
#5: Thank You card,
#6: Presentation Folder,
#7: Email signatures template (sample attached in word document)

Logo is attached. Logo can be reversed out (will attach once available). Logo can be stacked or horizontal (provided as horizontal).

Files need to be provided in ai + png format.

Target Market(s)

Business owners. More affluent.

Industry/Entity Type

Business

Requirements
Must have
• See brief

Font: Calibri
Should not have
• Photographs / stock photos

```html
<!DOCTYPE html>
<html lang="en">
<head>
<meta charset="utf-8">
<title>Northgate Insurance Brokers – Stationery</title>
<link href="https://fonts.googleapis.com/css2?family=Carlito:wght@400;700&display=swap" rel="stylesheet">
<style>
  :root{
    --green:#6b9b3a;
    --dark:#2b2d2b;
    --mid:#555756;
    --grey:#cfd0cf;
    --text:#3a3a3a;
    --paper:#fafbf3;
    --bg-top:#c9cacd;
    --bg-bottom:#a6a7ab;
  }
  *{box-sizing:border-box;margin:0;padding:0}
  html,body{width:1200px;height:1200px;overflow:hidden}
  body{
    position:relative;
    font-family:"Carlito",Calibri,sans-serif;
    color:var(--text);
    background:radial-gradient(ellipse at 50% 40%,var(--bg-top),var(--bg-bottom));
  }
  .piece{position:absolute;overflow:hidden}

  /* Brand lockup */
  .brand{display:flex;align-items:center;gap:7px;color:var(--green);font-weight:400;line-height:1}
  .brand .mark{background:var(--green);flex:none}
  .brand .name{display:flex;flex-direction:column}
  .brand .name .main{letter-spacing:.5px}
  .brand .name .sub{text-align:right;letter-spacing:.6px}

  /* Envelope */
  .envelope-back{left:85px;top:91px;width:367px;height:234px;background:#f1f2ec}
  .envelope-flap{position:absolute;left:0;top:0;width:367px;height:58px}
  .envelope-front{left:138px;top:182px;width:366px;height:183px;background:var(--paper)}
  .envelope-front .return{position:absolute;left:10px;top:10px;font-size:7px;line-height:1.2;color:#555}
  .envelope-front .rule{height:1px;background:#888;margin:4px 0 3px;width:86px}

  /* Letterhead */
  .letterhead{left:83px;top:385px;width:356px;height:505px;background:var(--paper)}
  .lh-header{height:60px;background:var(--grey);display:flex;align-items:center;padding-left:10px;border-bottom:2px solid var(--green)}
  .lh-divider{width:1px;height:44px;background:#777;margin:0 22px 0 20px}
  .lh-contact{font-size:6.2px;line-height:1.35;text-align:center;color:#555}
  .lh-contact .web{margin-top:3px}
  .lh-body{padding:45px 24px 0 54px;font-size:7.2px;line-height:1.45;text-align:justify}
  .lh-body p{margin-bottom:9px}
  .lh-watermark{position:absolute;left:92px;top:442px;opacity:.09}
  .lh-foot{position:absolute;left:0;bottom:0;width:100%;height:9px;background:var(--green)}

  /* Email signature */
  .signature{left:83px;top:930px;width:391px;height:105px;background:var(--paper);padding:12px 10px}
  .signature .who{font-size:14px;line-height:1}
  .signature .role{font-size:11.5px;color:#555;margin-bottom:5px}
  .signature .line{font-size:6px;margin-bottom:6px;white-space:nowrap}
  .signature .foot{display:flex;align-items:center;gap:22px}
  .signature .addr{font-size:7.5px;line-height:1.3;color:#555}

  /* ID badge */
  .badge{left:452px;top:460px;width:128px;height:191px;background:rgba(245,246,240,.85);border:1px solid #ccc;border-radius:4px;padding:22px 8px 8px}
  .badge .clip{position:absolute;left:52px;top:-2px;width:22px;height:16px;background:#c9cacc;border-radius:3px}
  .badge .card{background:var(--paper);height:160px;position:relative}
  .badge .top{background:var(--dark);height:28px;display:flex;align-items:center;padding-left:4px}
  .badge .who{text-align:center;font-size:15px;margin-top:10px;line-height:1}
  .badge .role{text-align:center;font-size:10.5px;color:#555}
  .badge .photo{position:absolute;left:20px;top:100px;width:84px;height:52px;background:linear-gradient(#e8ead8,#b9bcb0)}
  .badge .band{position:absolute;left:0;bottom:0;width:100%;height:6px;background:var(--green)}

  /* Folder */
  .folder-cover{left:579px;top:77px;width:569px;height:376px;background:var(--dark)}
  .folder-spine{position:absolute;left:284px;top:0;width:3px;height:100%;background:#3c3e3c}
  .folder-cover .brand{position:absolute;left:314px;top:99px}
  .folder-cover .band-wide{position:absolute;left:287px;top:269px;width:282px;height:66px;background:var(--green)}
  .folder-cover .band-thin{position:absolute;left:287px;top:353px;width:282px;height:12px;background:var(--green)}
  .folder-inside{left:580px;top:460px;width:569px;height:375px;background:var(--mid)}
  .folder-inside .pocket{position:absolute;left:0;top:224px;width:100%;height:151px;background:var(--dark)}
  .folder-inside .split{position:absolute;left:284px;top:0;width:2px;height:100%;background:#3e403e}
  .folder-inside .brand{position:absolute;left:312px;top:270px}
  .insert{position:absolute;left:12px;top:11px;width:259px;height:213px;background:var(--paper)}
  .insert .lh-header{height:42px;padding-left:6px}
  .insert .lh-divider{height:32px;margin:0 12px}
  .insert .lh-contact{font-size:4.3px}
  .insert .lh-body{padding:30px 16px 0 38px;font-size:5px;line-height:1.4}
  .insert .lh-body p{margin-bottom:6px}

  /* Business cards */
  .card-front{left:569px;top:855px;width:279px;height:147px;background:#7a7b7a}
  .card-front .face{position:absolute;left:13px;top:0;width:253px;height:147px;background:var(--grey);border-top:11px solid var(--green);border-bottom:11px solid var(--green)}
  .card-front .brand,.card-dark .brand{position:absolute;left:30px;top:47px}
  .card-back{left:865px;top:855px;width:274px;height:147px;background:var(--green)}
  .card-back .rail{position:absolute;left:0;top:0;width:62px;height:100%;background:var(--grey)}
  .card-back .rail .mark{position:absolute;left:14px;top:108px;width:32px;height:30px;background:var(--green)}
  .card-back .rail .vertical{position:absolute;left:6px;top:100px;transform:rotate(-90deg);transform-origin:left top;color:var(--green);font-size:17px;white-space:nowrap;line-height:1}
  .card-back .rail .vertical small{display:block;font-size:7px;text-align:right;color:#666}
  .card-back .rail .edge{position:absolute;right:0;top:0;width:12px;height:100%;background:#7a7b7a}
  .card-info{position:absolute;left:62px;top:0;right:0;bottom:0;color:#2e3a22}
  .card-info .who{position:absolute;top:20px;width:100%;text-align:center;font-size:19px;line-height:1}
  .card-info .role{position:absolute;top:45px;width:100%;text-align:center;font-size:14px}
  .card-info .left{position:absolute;left:18px;top:79px;font-size:7.3px;line-height:1.3}
  .card-info .left .gap{height:7px}
  .card-info .sep{position:absolute;left:120px;top:79px;width:1px;height:50px;background:#2e3a22;opacity:.5}
  .card-info .right{position:absolute;right:10px;top:79px;font-size:7.3px;line-height:1.65;text-align:right}
  .card-dark{left:569px;top:1015px;width:280px;height:147px;background:var(--dark);border-bottom:11px solid var(--green)}
  .card-dark-back{left:865px;top:1015px;width:280px;height:147px;background:var(--mid)}
  .card-dark-back .rail{position:absolute;left:0;top:0;width:63px;height:100%;background:var(--dark)}
  .card-dark-back .rail .edge{position:absolute;right:0;top:0;width:6px;height:100%;background:#3e403e}
  .card-dark-back .brand{position:absolute;left:9px;top:6px}
  .card-dark-back .card-info{left:63px;color:var(--green)}
  .card-dark-back .card-info .who{top:59px;font-size:11.5px}
  .card-dark-back .card-info .role{top:72px;font-size:8px}
  .card-dark-back .card-info .left{left:5px;top:95px;font-size:5.6px}
  .card-dark-back .card-info .left .gap{height:5px}
  .card-dark-back .card-info .sep{left:117px;top:96px;height:44px;background:var(--green)}
  .card-dark-back .card-info .right{top:93px;font-size:5.6px;line-height:1.55;right:3px}
</style>
</head>
<body>

<!-- Envelope -->
<div class="piece envelope-back">
  <svg class="envelope-flap" viewBox="0 0 367 58" aria-hidden="true">
    <defs><linearGradient id="flap" x1="0" y1="0" x2="0" y2="1"><stop offset="0" stop-color="#d8d9dc"/><stop offset="1" stop-color="#8e8f93"/></linearGradient></defs>
    <polygon points="18,0 349,0 367,52 367,58 0,58 0,52" fill="url(#flap)"/>
  </svg>
</div>
<div class="piece envelope-front">
  <div class="return">
    <div class="brand"><span class="mark" style="width:20px;height:19px"></span><span class="name"><span class="main" style="font-size:13px">Northgate</span><span class="sub" style="font-size:4px">Insurance Brokers</span></span></div>
    <div class="rule"></div>
    <div style="padding-left:24px;font-size:7px">Daniel Moss</div>
    <div style="padding-left:26px;font-size:3.5px;margin-bottom:3px">President &amp; CEO</div>
    <div>2280 Larch Road NW</div>
    <div>Calder, AB T5X 1K8</div>
  </div>
</div>

<!-- Letterhead -->
<div class="piece letterhead">
  <div class="lh-header">
    <div class="brand"><span class="mark" style="width:42px;height:44px"></span><span class="name"><span class="main" style="font-size:31px">Northgate</span><span class="sub" style="font-size:10.5px">Insurance Brokers</span></span></div>
    <div class="lh-divider"></div>
    <div class="lh-contact">
      <div>2280 Larch Road NW<br>Calder, AB T5X 1K8</div>
      <div style="margin-top:4px">Phone: 555.210.4400<br>Fax: 555.210.4401<br>Toll Free: 800.555.0142</div>
      <div class="web">www.northgatebrokers.com</div>
    </div>
  </div>
  <div class="lh-body">
    <p>Lorem ipsum dolor sit amet,</p>
    <p>scelerisque. Nam sapien odio, posuere ut ornare eget, sodales eget nibh. Nunc sed nunc lectus. Donec pharetra lobortis nulla, sit amet laoreet mauris ultricies at. Nulla tristique dui hendrerit urna rhoncus pellentesque. Cras vestibulum consectetur arcu, nec faucibus odio auctor at. Curabitur id congue ex. In lobortis vel risus quis porttitor. Vestibulum pellentesque quis tellus sed congue. Curabitur tristique posuere massa, id ultrices nulla tempus tincidunt. Vivamus sit amet enim sem. Quisque porta interdum arcu, sed dapibus magna. Praesent facilisis enim ac ante gravida rutrum.</p>
    <p>Phasellus vel lectus aliquam dui elementum lacinia. Donec et orci iaculis, rutrum augue eget, elementum leo. Curabitur congue libero id mi pulvinar porta. Ut varius enim cursus, lobortis leo sed, facilisis mi. Vivamus pellentesque id ipsum pharetra condimentum. Ut vitae commodo tellus. In eget eros sit amet velit tincidunt ornare. Sed mollis dolor eu condimentum mollis. Mauris vel blandit arcu. Aenean nec placerat lectus. Curabitur placerat id tortor nec consectetur. Nunc sed elit purus. Ut tellus eros, ullamcorper tristique odio quis, elementum molestie urna. Class aptent taciti sociosqu ad litora torquent per conubia nostra, per inceptos himenaeos.</p>
    <p>Maecenas iaculis vulputate dignissim. Nullam lorem felis, mattis vel libero a, imperdiet facilisis orci. Nullam facilisis mi eu arcu ultricies, ac sagittis sem tempus. Proin ullamcorper neque eu mi dapibus, vitae consequat lacus aliquet. Proin posuere ex nec tempus faucibus. Aenean scelerisque nisi justo, sit amet cursus leo euismod ut. Morbi maximus, sapien quis tincidunt ornare, quam nibh hendrerit mauris, id ultricies lorem orci vel dui. Phasellus consectetur sapien a risus convallis dapibus. Sed a tempor libero. Nam quis libero ligula. Morbi eget velit eu sapien finibus iaculis nec tincidunt orci. Donec sodales erat laoreet nisl interdum volutpat.</p>
    <p style="margin-top:30px">Morbi eget velit eu</p>
  </div>
  <div class="lh-watermark brand"><span class="mark" style="width:42px;height:40px"></span><span class="name"><span class="main" style="font-size:29px">Northgate</span><span class="sub" style="font-size:9.5px">Insurance Brokers</span></span></div>
  <div class="lh-foot"></div>
</div>

<!-- Email signature -->
<div class="piece signature">
  <div class="who">Daniel Moss, BA, CRM</div>
  <div class="role">President &amp; CEO</div>
  <div class="line">Direct: 555.210.4499 | Phone: 555.210.4400 | Fax: 555.210.4401 | Toll Free: 800.555.0142 | dmoss@northgatebrokers.com</div>
  <div class="foot">
    <div class="brand"><span class="mark" style="width:22px;height:34px"></span><span class="name"><span class="main" style="font-size:22px">Northgate</span><span class="sub" style="font-size:7.5px">Insurance Brokers</span></span></div>
    <div class="addr">2280 Larch Road NW<br>Calder, AB T5X 1K8</div>
  </div>
</div>

<!-- ID badge -->
<div class="piece badge">
  <div class="clip"></div>
  <div class="card">
    <div class="top"><div class="brand"><span class="mark" style="width:16px;height:16px"></span><span class="name"><span class="main" style="font-size:14px">Northgate</span><span class="sub" style="font-size:4px">Insurance Brokers</span></span></div></div>
    <div class="who">Daniel Moss</div>
    <div class="role">President &amp; CEO</div>
    <div class="photo" role="img" aria-label="Staff portrait photo area"></div>
    <div class="band"></div>
  </div>
</div>

<!-- Presentation folder, outside -->
<div class="piece folder-cover">
  <div class="folder-spine"></div>
  <div class="brand"><span class="mark" style="width:54px;height:52px"></span><span class="name"><span class="main" style="font-size:36px">Northgate</span><span class="sub" style="font-size:11.5px">Insurance Brokers</span></span></div>
  <div class="band-wide"></div>
  <div class="band-thin"></div>
</div>

<!-- Presentation folder, inside -->
<div class="piece folder-inside">
  <div class="insert">
    <div class="lh-header">
      <div class="brand"><span class="mark" style="width:28px;height:30px"></span><span class="name"><span class="main" style="font-size:21px">Northgate</span><span class="sub" style="font-size:7px">Insurance Brokers</span></span></div>
      <div class="lh-divider"></div>
      <div class="lh-contact">
        <div>2280 Larch Road NW<br>Calder, AB T5X 1K8</div>
        <div style="margin-top:3px">Phone: 555.210.4400<br>Fax: 555.210.4401<br>Toll Free: 800.555.0142</div>
        <div class="web">www.northgatebrokers.com</div>
      </div>
    </div>
    <div class="lh-body">
      <p>Lorem ipsum dolor sit amet,</p>
      <p>scelerisque. Nam sapien odio, posuere ut ornare eget, sodales eget nibh. Nunc sed nunc lectus. Donec pharetra lobortis nulla, sit amet laoreet mauris ultricies at. Nulla tristique dui hendrerit urna rhoncus pellentesque. Cras vestibulum consectetur arcu, nec faucibus odio auctor at. Curabitur id congue ex. In lobortis vel risus quis porttitor. Vestibulum pellentesque quis tellus sed congue. Curabitur tristique posuere massa, id ultrices nulla tempus tincidunt. Vivamus sit amet enim sem. Quisque porta interdum arcu, sed dapibus magna. Praesent facilisis enim ac ante gravida rutrum.</p>
      <p>Phasellus vel lectus aliquam dui elementum lacinia. Donec et orci iaculis, rutrum augue eget, elementum leo. Curabitur congue libero id mi pulvinar porta. Ut varius enim cursus, lobortis leo sed, facilisis mi. Vivamus pellentesque id ipsum pharetra condimentum. Ut vitae commodo tellus. In eget eros sit amet velit tincidunt ornare. Sed mollis dolor eu condimentum mollis. Mauris vel blandit arcu. Aenean nec placerat lectus. Curabitur placerat id tortor nec consectetur. Nunc sed elit purus. Ut tellus eros, ullamcorper tristique odio quis, elementum molestie urna.</p>
    </div>
  </div>
  <div class="split"></div>
  <div class="pocket"></div>
  <div class="brand"><span class="mark" style="width:54px;height:52px"></span><span class="name"><span class="main" style="font-size:36px">Northgate</span><span class="sub" style="font-size:11.5px">Insurance Brokers</span></span></div>
</div>

<!-- Business card, light front -->
<div class="piece card-front">
  <div class="face"></div>
  <div class="brand"><span class="mark" style="width:50px;height:53px"></span><span class="name"><span class="main" style="font-size:34px">Northgate</span><span class="sub" style="font-size:11.5px">Insurance Brokers</span></span></div>
</div>

<!-- Business card, green back -->
<div class="piece card-back">
  <div class="rail">
    <div class="vertical">Northgate<small>Insurance Brokers</small></div>
    <div class="mark"></div>
    <div class="edge"></div>
  </div>
  <div class="card-info">
    <div class="who">Daniel Moss, BA, CRM</div>
    <div class="role">President &amp; CEO</div>
    <div class="left">2280 Larch Road NW<br>Calder, AB T5X 1K8<div class="gap"></div>dmoss@northgatebrokers.com<br>www.northgatebrokers.com</div>
    <div class="sep"></div>
    <div class="right">Phone: 555.210.4400<br>Direct: 555.210.4499<br>Fax: 555.210.4401<br>Toll Free: 800.555.0142</div>
  </div>
</div>

<!-- Business card, dark front -->
<div class="piece card-dark">
  <div class="brand"><span class="mark" style="width:50px;height:53px"></span><span class="name"><span class="main" style="font-size:34px">Northgate</span><span class="sub" style="font-size:11.5px">Insurance Brokers</span></span></div>
</div>

<!-- Business card, dark back -->
<div class="piece card-dark-back">
  <div class="rail"><div class="edge"></div></div>
  <div class="brand"><span class="mark" style="width:40px;height:36px"></span><span class="name"><span class="main" style="font-size:25px">Northgate</span><span class="sub" style="font-size:8.5px">Insurance Brokers</span></span></div>
  <div class="card-info">
    <div class="who">Daniel Moss, BA, CRM</div>
    <div class="role">President &amp; CEO</div>
    <div class="left">2280 Larch Road NW<br>Calder, AB T5X 1K8<div class="gap"></div>dmoss@northgatebrokers.com<br>www.northgatebrokers.com</div>
    <div class="sep"></div>
    <div class="right">Phone: 555.210.4400<br>Direct: 555.210.4499<br>Fax: 555.210.4401<br>Toll Free: 800.555.0142</div>
  </div>
</div>

</body>
</html>
```